Leaf By Frost - Stationery Design Project

Hi everyone,

We need a business card and a stationary set designed for a new corporate video production company based in Sydney, 'Leaf By Frost'.

The name refers to the mythological 'phoenix' so we would like to see designs that are appropriate to both the name and to a creative film company. The key thing is, we need to appear fresh and creative while maintaining professionalism.

We would like to stick with dark colors for the basis of the card. One idea that came up was obsidian/volcanic rock with the logo cracking through to reveal lava or something fire like. This is just one idea that has come up, but we are of course open to others and would love to see what people can come up with. Extensive use of flames/fire imagery is not really what we are after.

Also, cinematic as opposed to corporate is preferable.

**** UPDATE ****
When I hand over the card to a prospective client, I want them to feel like they are receiving an obsidian plate with inscriptions in it (ie the phoenix). Looking for something elemental and rigid to contrast and complement the graceful lines of the logo.

Designs we require:
- Business card
(We would like a business card that makes use of some of the more premium business card printing options, such as foil stamping, embossing/debossing, painted edges, spot UV etc. Doesnt have to use all these things, only what you feel works, but we are looking for a business card that stands out and is memorable and these nice touches have that effect. For an example of what is possible, check out "http://www.glossvantage.example/base/category/business-card-gallery/".)

- Letter head
- With compliments slip
- Display folder

COPMPANY DETAILS:
ABN: 52 804 319 246
Company Address: 7/18-20 Hollin Ave, Kelmore NSW 2094
Name: Rob K. Deverill
Title: Producer
Contact Number: 0417 352 918
email: rob@leafbyfrost.example
website: www.leafbyfrost.example

ABOUT THE PHOENIX:
The phoenix is a musical bird from mythology, known for its long fancy tail and small plume on the top of its head. They are elegant and graceful and symbolize immortality, endurance and strength, believed to live for 5 centuries before they were reborn from their ashes.
Updates

Hi everyone,

We have just updated the design brief to include business contact information, website etc. should anyone require it for their designs.

Thanks

Rob

Target Market(s)

Other creative businesses and marketing firms.

Industry/Entity Type

Printing

Requirements
Must have
• Basic printing requirements:
- CMYK colour space
- 300dpi resolution
- Color bleed/crop marks etc to allow for trimming where necessary
- Source files upon handover
Should not have
• Overuse of fire/flame imagery

```html
<!DOCTYPE html>
<html lang="en">
<head>
<meta charset="utf-8">
<title>Leaf By Frost — Stationery Set</title>
<link href="https://fonts.googleapis.com/css2?family=Source+Sans+3:wght@400;500;600;700&display=swap" rel="stylesheet">
<style>
  :root {
    --board: #707173;
    --obsidian: #000000;
    --ember: #d2232a;
    --ember-deep: #8e1116;
    --paper: #ffffff;
    --mist: #eeecec;
    --ink: #111111;
  }
  * { margin: 0; padding: 0; box-sizing: border-box; }
  html, body {
    width: 1200px; height: 975px; overflow: hidden;
    background: var(--board);
    font-family: "Source Sans 3", sans-serif;
  }
  .board { position: relative; width: 1200px; height: 975px; }
  .piece { position: absolute; overflow: hidden; }
  .dark { background: var(--obsidian); color: var(--paper); }
  .caps { text-transform: uppercase; }
  .red { color: var(--ember); }
  .line { position: absolute; white-space: nowrap; }

  /* sweeping artwork areas: red plumage with white accents */
  .art {
    position: absolute;
    background:
      radial-gradient(ellipse 34% 22% at 30% 72%, rgba(255,255,255,0.55) 0%, rgba(255,255,255,0) 100%),
      radial-gradient(ellipse 18% 26% at 78% 90%, rgba(210,35,42,0.95) 0%, rgba(210,35,42,0) 100%),
      radial-gradient(ellipse 55% 60% at 22% 28%, var(--ember) 0%, var(--ember-deep) 45%, rgba(0,0,0,0) 100%);
  }

  /* business card front */
  .card-front { left: 35px; top: 27px; width: 234px; height: 135px; }
  .card-front .art { left: 0; top: 0; width: 170px; height: 135px; }
  .card-front .brand { left: 101px; top: 59px; font-size: 9px; letter-spacing: 4.2px; font-weight: 600; }
  .card-front .web { left: 107px; top: 72px; font-size: 7px; letter-spacing: 1.2px; }

  /* business card back */
  .card-back { left: 276px; top: 27px; width: 233px; height: 135px; }
  .card-back .art { right: 0; top: 0; width: 90px; height: 135px;
    background:
      radial-gradient(ellipse 60% 18% at 55% 88%, rgba(255,255,255,0.55) 0%, rgba(255,255,255,0) 100%),
      radial-gradient(ellipse 55% 55% at 80% 30%, var(--ember) 0%, var(--ember-deep) 45%, rgba(0,0,0,0) 100%); }
  .card-back .name { left: 12px; top: 20px; font-size: 8.5px; font-weight: 700; letter-spacing: 0.8px; }
  .card-back .role { left: 12px; top: 31px; font-size: 7px; letter-spacing: 1.6px; }
  .card-back .rule { position: absolute; left: 0; top: 44px; width: 187px; height: 1px; background: var(--paper); }
  .card-back .detail { left: 12px; font-size: 6.8px; letter-spacing: 1.4px; }
  .card-back .abn { left: 12px; top: 114px; font-size: 5.6px; letter-spacing: 1px; }

  /* compliments slip */
  .slip { left: 606px; top: 18px; width: 543px; height: 256px; }
  .slip .art { left: 0; top: 0; width: 270px; height: 256px; }
  .slip .address { right: 22px; top: 16px; text-align: right; font-size: 10.5px; letter-spacing: 2.2px; line-height: 14px; }
  .slip .brand { left: 182px; top: 121px; font-size: 19px; letter-spacing: 10.6px; font-weight: 500; }
  .slip .web { left: 195px; top: 149px; font-size: 15px; letter-spacing: 1.9px; }
  .slip .email { right: 22px; top: 227px; font-size: 11px; letter-spacing: 2px; }
  .slip .abn { right: 22px; top: 243px; font-size: 9px; letter-spacing: 1.8px; }

  /* letterhead */
  .letterhead { left: 35px; top: 178px; width: 544px; height: 768px; background: var(--paper); }
  .letterhead .masthead { position: absolute; left: 195px; top: 0; width: 155px; height: 116px; }
  .letterhead .masthead .mark { position: absolute; left: 56px; top: 18px; width: 44px; height: 44px; border-radius: 50%; background: var(--ember); }
  .letterhead .masthead .brand { left: 0; width: 155px; top: 95px; text-align: center; font-size: 9px; letter-spacing: 5.5px; font-weight: 600; }
  .letterhead .watermark { position: absolute; left: 0; top: 250px; width: 400px; height: 500px;
    background:
      radial-gradient(ellipse 40% 45% at 28% 38%, var(--mist) 0%, rgba(238,236,236,0) 100%),
      radial-gradient(ellipse 30% 35% at 78% 55%, #f2f2f2 0%, rgba(242,242,242,0) 100%); }
  .letterhead .contact { right: 18px; top: 676px; text-align: right; font-size: 8.5px; letter-spacing: 1.8px; line-height: 11px; color: var(--ink); }
  .letterhead .footer-rule { position: absolute; left: 0; top: 746px; width: 100%; height: 3px; background: var(--ember); }
  .letterhead .footer-band { position: absolute; left: 0; top: 749px; width: 100%; height: 19px; background: var(--obsidian); }
</style>
</head>
<body>
<main class="board">

  <section class="piece dark card-front" aria-label="Business card front">
    <div class="art" role="img" aria-label="Phoenix line artwork in red and white sweeping strokes"></div>
    <p class="line brand caps">Leaf By Frost</p>
    <p class="line web caps red">www.leafbyfrost.example</p>
  </section>

  <section class="piece dark card-back" aria-label="Business card back">
    <div class="art" role="img" aria-label="Phoenix tail feathers in red and white sweeping strokes"></div>
    <p class="line name caps">Rob K. Deverill</p>
    <p class="line role caps red">Producer</p>
    <div class="rule"></div>
    <p class="line detail caps" style="top:58px">7/18-20 Hollin Ave,</p>
    <p class="line detail caps" style="top:67px">Kelmore NSW 2094</p>
    <p class="line detail" style="top:80px">0417 352 918</p>
    <p class="line detail caps red" style="top:104px">rob@leafbyfrost.example</p>
    <p class="line abn">ABN: 52 804 319 246</p>
  </section>

  <section class="piece dark slip" aria-label="With compliments slip">
    <div class="art" role="img" aria-label="Phoenix line artwork in red and white sweeping strokes"></div>
    <p class="line address caps">7/18-20 Hollin Ave,<br>Kelmore NSW 2094<br>0417 352 918</p>
    <p class="line brand caps">Leaf By Frost</p>
    <p class="line web caps red">www.leafbyfrost.example</p>
    <p class="line email caps red">rob@leafbyfrost.example</p>
    <p class="line abn">ABN: 52 804 319 246</p>
  </section>

  <section class="piece letterhead" aria-label="Letterhead">
    <div class="masthead dark">
      <span class="mark" aria-hidden="true"></span>
      <p class="line brand caps">Leaf By Frost</p>
    </div>
    <div class="watermark" role="img" aria-label="Faint grey phoenix line artwork"></div>
    <p class="line contact">ABN: 52 804 319 246<br><span class="caps">7/18-20 Hollin Ave,</span><br><span class="caps">Kelmore NSW 2094</span><br>0417 352 918<br><span class="caps red">rob@leafbyfrost.example</span><br><span class="caps red">www.leafbyfrost.example</span></p>
    <div class="footer-rule"></div>
    <div class="footer-band"></div>
  </section>

</main>
</body>
</html>
```